Brochure & Business card design

Looking for a new business card design i want it to be modern and sharp looking i usually order plastic business cards, and i would like to make the colors like the logo teal/charcoal i will like to have our services on icons with words.... our services are
ROOFING GUTTERS PAINTING PRESSURE WASHING EXTERIOR DESIGN & ATTIC VENTILATION. I also want to add my credentials

Target Market(s)

Oregon local market

Industry/Entity Type

Residential Construction

Contact Information for Business Card

Business info, services, number, website

Font styles to use
Serif
Sans Serif

Colors
33b8a4
5c5c5c
ffffff

Requirements
Must have
• Tomas Relke
• Cell:
• Office:
• Email:
• Website:
• also i need our social media icons
• Services ROOFING GUTTERS PAINTING PRESSURE WASHING EXTERIOR DESIGN & ATTIC VENTILATION
• -icons for number, web, email, cell
• OR #384152
• Wa #KTRAPLD547Q3
Nice to have
• -Clean design Front & Back
• -Icons
• -shape House just like logo design
• -First Impression
Should not have
• Not Busy or lost of eye contact

```html
<!DOCTYPE html>
<html lang="en">
<head>
<meta charset="utf-8">
<title>Ridgeline Home Exteriors — Business Card</title>
<link rel="stylesheet" href="https://fonts.googleapis.com/css2?family=EB+Garamond:wght@400;500;600&display=swap">
<style>
  :root {
    --teal: #1f9a8a;
    --teal-light: #33b8a4;
    --charcoal: #5c5c5c;
    --ink: #2b2b2b;
    --card-dark: #232323;
    --card-light: #f3f4f4;
    --band: #1e1e1e;
    --white: #ffffff;
    --page: #efefef;
    --serif: "EB Garamond", Georgia, serif;
  }
  * { margin: 0; padding: 0; box-sizing: border-box; }
  html, body { width: 1200px; height: 757px; overflow: hidden; background: var(--page); }
  .canvas { position: relative; width: 1200px; height: 757px; font-family: var(--serif); }

  .card { position: absolute; top: 195px; width: 499px; height: 299px; overflow: hidden; }

  /* Front */
  .card--front { left: 85px; background: var(--card-dark); color: var(--white); }
  .front-brand {
    position: absolute; left: 0; right: 0; top: 98px;
    display: flex; flex-direction: column; align-items: center; gap: 2px;
  }
  .front-brand .mark { width: 14px; height: 14px; background: var(--white); margin-bottom: 10px; }
  .front-brand .brand-name {
    font-size: 30px; font-weight: 500; letter-spacing: 0.5px; color: var(--white); line-height: 1;
  }
  .front-brand .brand-sub {
    font-size: 19px; font-weight: 500; letter-spacing: 1.5px; color: var(--white); text-transform: uppercase;
  }
  .front-web {
    position: absolute; left: 0; right: 0; top: 263px; text-align: center;
    font-size: 11px; font-weight: 600; letter-spacing: 3.4px;
  }

  /* Back */
  .card--back { left: 650px; background: var(--card-light); color: var(--ink); }
  .person { position: absolute; left: 31px; top: 93px; }
  .person .name { font-size: 18px; font-weight: 600; color: var(--teal); letter-spacing: 0.3px; line-height: 1.1; }
  .person .role { font-size: 10px; color: var(--ink); margin-top: 3px; }
  .person .site { font-size: 11.5px; font-weight: 600; color: var(--ink); margin-top: 6px; }
  .person .site span { color: var(--teal); }

  .contacts { position: absolute; left: 31px; top: 183px; list-style: none; }
  .contacts li { display: flex; align-items: center; gap: 7px; font-size: 10.5px; height: 19.5px; }
  .contacts svg { width: 10px; height: 10px; fill: var(--teal); flex: none; }

  .back-brand {
    position: absolute; left: 285px; width: 200px; top: 108px;
    display: flex; flex-direction: column; align-items: center;
  }
  .back-brand .mark { width: 14px; height: 14px; background: var(--charcoal); margin-bottom: 10px; }
  .back-brand .brand-name { font-size: 28px; font-weight: 500; color: var(--teal); line-height: 1; }
  .back-brand .brand-sub { font-size: 18px; font-weight: 500; color: var(--teal); letter-spacing: 1.2px; text-transform: uppercase; }

  .badges { position: absolute; left: 396px; top: 251px; display: flex; gap: 5px; }
  .badge { width: 40px; height: 14px; }
  .badge--dark { background: var(--ink); }
  .badge--red { background: #c8282c; }

  .services-band {
    position: absolute; left: 0; right: 0; bottom: 0; height: 25px;
    background: var(--band); color: var(--white);
    display: flex; align-items: center; justify-content: center; gap: 5px;
    font-size: 10.5px; white-space: nowrap;
  }
  .services-band .label { font-weight: 600; font-size: 12px; text-decoration: underline; margin-right: 2px; }
</style>
</head>
<body>
<main class="canvas">

  <section class="card card--front" aria-label="Card front">
    <div class="front-brand">
      <span class="mark" aria-hidden="true"></span>
      <span class="brand-name">Ridgeline</span>
      <span class="brand-sub">Home Exteriors</span>
    </div>
    <p class="front-web">www.ridgelinehomes.com</p>
  </section>

  <section class="card card--back" aria-label="Card back">
    <div class="person">
      <p class="name">Tomas Relke</p>
      <p class="role">Owner &amp; Founder</p>
      <p class="site">www.<span>ridgelinehomes</span>.com</p>
    </div>

    <ul class="contacts">
      <li>
        <svg viewBox="0 0 10 10" aria-hidden="true"><path d="M2.5 0h5a1 1 0 0 1 1 1v8a1 1 0 0 1-1 1h-5a1 1 0 0 1-1-1V1a1 1 0 0 1 1-1zm.3 1.2v6.6h4.4V1.2z"/></svg>
        (+1) 482-73105
      </li>
      <li>
        <svg viewBox="0 0 10 10" aria-hidden="true"><path d="M0 3.5C0 2 2 1.5 5 1.5s5 .5 5 2v1H7.5v-1h-5v1H0zM2.5 5h5l1.5 4.5H1z"/></svg>
        (503) 614-2290
      </li>
      <li>
        <svg viewBox="0 0 10 10" aria-hidden="true"><path d="M0 2h10v6H0zm1 .8L5 5.6 9 2.8z"/></svg>
        tomas@ridgelinehomes.com
      </li>
    </ul>

    <div class="back-brand">
      <span class="mark" aria-hidden="true"></span>
      <span class="brand-name">Ridgeline</span>
      <span class="brand-sub">Home Exteriors</span>
    </div>

    <div class="badges" aria-label="Credentials">
      <span class="badge badge--dark"></span>
      <span class="badge badge--red"></span>
    </div>

    <div class="services-band">
      <span class="label">Our Services:</span>
      <span>Roofing | Gutters | Pressure Washing | Painting | Exterior Design | Attic Ventilation</span>
    </div>
  </section>

</main>
</body>
</html>
```